New solo practice law firm is looking for an elegant, professional, and interactive web design

I need a web design and developer for a new small law firm in Sacramento, California called Dorian Kessly Law, A Professional Corporation. I am a trial lawyer who represents average people facing difficult litigation disputes, including criminal defense as a former prosecutor and civil litigation as a civil litigator. Criminal defense includes domestic violence, battery, assault, drug possession, theft, DUI, etc. Civil litigation includes business disputes, property disputes, employment disputes, family law disputes, and immigration issues. I would like to see web designs that incorporate my logo and use the logo's navy blue and gold colors. I have uploaded the files of my logo to this brief. Please only use the navy blue and gold version. Overall, I want the design to look firm, professional, and elegant.

I plan on having the following pages on my website: (1) Home, (2) Dorian Kessly, (3) Practice Areas, (4) Insights, (5) Contact. I've hand drawn a preliminary sketch concept of what I envision the home page's layout to look like (attached with a text version). I would like your design to keep a similar layout for the homepage and incorporate my logo's colors within it but I am open to creative layout alternatives/ideas. I would like the other pages to have a similar look and feel as the home page. Some of the areas currently in my sketch do not have the full text. You can insert other text for now and I will provide the winner the full text.

In terms of the pictures on the website, I enjoy images of courthouses, columns (example attached but I cannot use this one), and, if possible, images from Sacramento, CA in my background (headshot attached). A plus would be live images that move and also sections of the webpage moving in the viewers view as they scroll down on the page. Also, it would be great to have my logo act as the tab for the website. I can provide other versions of the logo if needed.

I look forward to seeing your Wordpress designs!

People needing legal representation.

Law

Coded - Design and coding required

5+ page

Serif

• Incorporate my logo and my logo's colors.
• Live pictures and images appearing as viewers scroll on page.

```html
<!DOCTYPE html>
<html lang="en">
<head>
<meta charset="utf-8">
<title>Dorian Kessly Law</title>
<link rel="stylesheet" href="https://fonts.googleapis.com/css2?family=Montserrat:wght@300;400;500;600;700;800&display=swap">
<style>
:root{
  --navy:#14233e;
  --navy-deep:#0f1c33;
  --gold:#ad9467;
  --gold-light:#c8ad78;
  --ink:#1c2536;
  --text:#2b2f38;
  --muted:#6a6f78;
  --white:#ffffff;
  --charcoal:#2c2d31;
}
*{box-sizing:border-box;margin:0;padding:0}
html,body{width:1200px;height:2918px;overflow:hidden}
body{font-family:"Montserrat",Arial,sans-serif;color:var(--text);background:var(--white);position:relative}
.abs{position:absolute}

/* header */
.topbar{left:0;top:0;width:1200px;height:115px;background:var(--navy)}
.brand{left:108px;top:28px;display:flex;align-items:center;gap:16px}
.brand-mark{width:44px;height:44px;background:var(--gold)}
.brand-name{color:var(--gold);font-size:22px;font-weight:400;letter-spacing:4px;line-height:1.2}
.brand-name small{display:block;font-size:10px;letter-spacing:3px;margin-top:6px}
.address{left:627px;top:22px;color:var(--white);font-size:14.5px;line-height:24px;letter-spacing:.3px}
.consult{left:865px;top:0;width:335px;height:115px;background:var(--gold);padding:17px 0 0 37px;color:var(--white)}
.consult p{font-size:15px;letter-spacing:.3px}
.consult strong{display:block;font-size:20px;font-weight:700;margin-top:2px}
.lang{margin-top:10px;width:119px;height:27px;border:1px solid var(--white);font-size:10px;padding:6px 13px;position:relative}
.lang svg{position:absolute;right:10px;top:9px}

/* nav */
.mainnav{left:0;top:115px;width:1200px;height:56px;border-bottom:1px solid #e4e4e4;display:flex}
.mainnav a{position:absolute;top:0;height:56px;line-height:56px;font-size:15px;font-weight:600;color:var(--ink);text-decoration:none;text-transform:uppercase}
.mainnav a.active{color:var(--gold);border-bottom:3px solid var(--gold);padding:0 28px}

/* hero */
.hero{left:0;top:171px;width:1200px;height:592px;background:linear-gradient(180deg,#8c9dbb 0%,#c9cfdc 28%,#d2b58c 50%,#b38d5f 72%,#7b6a57 100%)}
.hero-arrow{top:220px}

/* intro */
.intro-icon{left:583px;top:797px;width:34px;height:34px;border:2px solid var(--navy)}
.intro-title{left:0;top:840px;width:1200px;text-align:center;font-size:32px;font-weight:300;color:var(--ink);letter-spacing:.3px}
.intro-title b{font-weight:800}
.intro-rule{left:551px;top:887px;width:98px;height:3px;background:var(--gold)}
.intro-text{left:0;top:908px;width:1200px;text-align:center;font-size:18px;line-height:28px;color:var(--ink)}

.card{top:1017px;width:233px}
.card-photo{width:231px;height:188px}
.card-label{font-size:16px;font-weight:700;color:var(--ink);letter-spacing:.5px;padding:10px 0 0 7px;height:40px;border-bottom:2px solid var(--gold)}

/* about band */
.about{left:0;top:1322px;width:1200px;height:575px;background:linear-gradient(100deg,#3a3b40 0%,#2a2b2f 40%,#1f2024 100%)}
.about-visual{left:576px;top:1322px;width:624px;height:575px;background:linear-gradient(135deg,#b39a68 0%,#8a7450 45%,#3a3a3e 100%)}
.about-title{left:126px;top:1428px;color:var(--white);font-size:38px;font-weight:300;line-height:44px}
.about-title b{font-weight:800;display:block}
.about-rule{left:126px;top:1526px;width:72px;height:3px;background:var(--gold)}
.about-copy{left:126px;top:1548px;width:410px;color:#e9e9ea;font-size:15.5px;line-height:24px}
.about-copy p+p{margin-top:17px}
.btn-outline{left:126px;top:1759px;width:188px;height:43px;border:2px solid var(--gold);color:var(--gold);font-size:14px;font-weight:700;display:flex;align-items:center;justify-content:center;gap:6px;letter-spacing:.5px}

/* consultation */
.contact-band{left:0;top:1897px;width:1200px;height:610px;background:linear-gradient(180deg,#15243f 0%,#1b2a47 55%,#111d33 100%)}
.form-frame{left:131px;top:1974px;width:457px;height:449px;border:2px solid var(--gold)}
.form-card{left:120px;top:1963px;width:457px;height:450px;background:var(--gold);padding:40px 0 0 47px}
.form-card h2{color:var(--white);font-size:22px;font-weight:800;line-height:24px;letter-spacing:.5px}
.field{width:374px;height:42px;border:2px solid var(--white);color:var(--white);font-size:12px;font-weight:600;padding:12px 16px;margin-top:10px}
.field:first-of-type{margin-top:18px}
.field.area{height:112px}
.submit{margin-top:14px;width:156px;height:42px;background:var(--navy);color:var(--white);font-size:14px;font-weight:700;display:flex;align-items:center;justify-content:center}
.contact-title{left:650px;top:2017px;color:var(--white);font-size:30px;font-weight:300;line-height:39px}
.contact-title b{font-weight:800;display:block}
.contact-rule{left:650px;top:2143px;width:77px;height:3px;background:var(--gold)}
.contact-copy{left:650px;top:2165px;width:460px;color:#e6e8ed;font-size:16px;line-height:26px}
.contact-copy p+p{margin-top:18px}

/* footer */
.foot-brand{left:130px;top:2555px;width:260px;text-align:center}
.foot-mark{width:60px;height:60px;background:var(--navy);margin:0 auto 70px}
.foot-name{font-size:19px;letter-spacing:3.5px;color:var(--navy);font-weight:400}
.foot-name small{display:block;font-size:9px;letter-spacing:2.5px;margin-top:5px}
.foot-col h3{color:var(--gold);font-size:16px;font-weight:700;letter-spacing:.5px}
.foot-col .rule{width:40px;height:2px;background:var(--gold);margin:8px 0 15px}
.foot-col p{font-size:13.5px;line-height:23px;color:var(--ink);padding-left:4px}
.social{display:flex;gap:8px;margin-top:22px;padding-left:4px}
.social span{width:30px;height:30px;border-radius:50%;background:var(--navy)}
.social span:first-child{background:var(--gold)}
.foot-divider{left:0;top:2787px;width:1200px;height:1px;background:#dcdcdc}
.disclaimer{left:122px;top:2811px;width:940px;font-size:13px;line-height:17px;color:var(--muted)}
.copyright{left:122px;top:2866px;font-size:12.5px;color:var(--muted)}
</style>
</head>
<body>

<header>
  <div class="abs topbar"></div>
  <div class="abs brand">
    <span class="brand-mark"></span>
    <div class="brand-name">DORIAN KESSLY LAW<small>A PROFESSIONAL CORPORATION</small></div>
  </div>
  <div class="abs address">4720 LARKFIELD AVE<br>SUITE #210<br>ELK GROVE, CA 95758</div>
  <div class="abs consult">
    <p>FREE CONSULTATION</p>
    <strong>(916) 555-0148</strong>
    <div class="lang">ENGLISH
      <svg width="11" height="7" viewBox="0 0 11 7"><path d="M1 1l4.5 4.5L10 1" fill="none" stroke="#fff" stroke-width="1.5"/></svg>
    </div>
  </div>
</header>

<nav class="abs mainnav">
  <a class="active" style="left:106px">Home</a>
  <a style="left:292px">Dorian Kessly</a>
  <a style="left:543px">Practice Areas</a>
  <a style="left:781px">Insights</a>
  <a style="left:963px">Contact</a>
</nav>

<section>
  <div class="abs hero" role="img" aria-label="Classical courthouse with marble columns and wide steps under a streaked sky"></div>
  <svg class="abs hero-arrow" style="left:50px;top:396px" width="30" height="54" viewBox="0 0 30 54"><path d="M28 2L3 27l25 25" fill="none" stroke="#fff" stroke-width="3"/></svg>
  <svg class="abs hero-arrow" style="left:1135px;top:396px" width="30" height="54" viewBox="0 0 30 54"><path d="M2 2l25 25L2 52" fill="none" stroke="#fff" stroke-width="3"/></svg>
</section>

<section>
  <div class="abs intro-icon"></div>
  <h1 class="abs intro-title">CRIMINAL AND <b>CIVIL TRIAL LAWYERS</b></h1>
  <div class="abs intro-rule"></div>
  <p class="abs intro-text">Dorian Kessly Law is a law firm serving the Sacramento, Yolo, San Joaquin, Solano and Stanislaus Counties.<br>We represent clients in a wide array of criminal, civil, family law, and immigration cases</p>

  <div class="abs card" style="left:115px">
    <div class="card-photo" role="img" aria-label="Hands in handcuffs" style="background:linear-gradient(160deg,#5a4a3f,#b78a6c 50%,#3a3230)"></div>
    <div class="card-label">CRIMINAL DEFENSE</div>
  </div>
  <div class="abs card" style="left:361px">
    <div class="card-photo" role="img" aria-label="Lawyer in a suit signing documents beside a gavel" style="background:linear-gradient(160deg,#2a2a2e,#4a4a52 55%,#d8d6d2)"></div>
    <div class="card-label">CIVIL LITIGATION</div>
  </div>
  <div class="abs card" style="left:608px">
    <div class="card-photo" role="img" aria-label="Open desert road under cloudy sky" style="background:linear-gradient(180deg,#8796ae,#c9c7c2 40%,#8d7c6a 55%,#3c3b3c)"></div>
    <div class="card-label">IMMIGRATION</div>
  </div>
  <div class="abs card" style="left:855px">
    <div class="card-photo" role="img" aria-label="Young family outdoors in sunlight" style="background:linear-gradient(160deg,#f0e3c8,#c8b27f 45%,#6f8a4e)"></div>
    <div class="card-label">FAMILY LAW</div>
  </div>
</section>

<section>
  <div class="abs about" role="img" aria-label="Dim city buildings in the background"></div>
  <div class="abs about-visual" role="img" aria-label="Attorney portrait in a dark suit against a gold backdrop"></div>
  <h2 class="abs about-title">READY, RELIABLE,<b>AND EXPERIENCED</b></h2>
  <div class="abs about-rule"></div>
  <div class="abs about-copy">
    <p>Lorem ipsum dolor sit amet, consectetur adipiscing elit, sed do eiusmod tempor incididunt ut labore et dolore magna aliqua. orem ipsum dolor sit amet, consectetur adipiscing elit, sed do eiusmod tempor incididunt ut labore et dolore magna aliqua.</p>
    <p>Ut enim ad minim veniam, quis nostrud exercitation ullamco laboris nisi ut aliquip</p>
  </div>
  <div class="abs btn-outline">ABOUT DORIAN
    <svg width="8" height="12" viewBox="0 0 8 12"><path d="M1 1l5 5-5 5" fill="none" stroke="currentColor" stroke-width="2"/></svg>
  </div>
</section>

<section>
  <div class="abs contact-band" role="img" aria-label="Sacramento tower bridge over the river at dusk, tinted navy"></div>
  <div class="abs form-frame"></div>
  <form class="abs form-card">
    <h2>SCHEDULE A FREE<br>CONSULATION</h2>
    <div class="field">Name</div>
    <div class="field">Email</div>
    <div class="field">Phone Number</div>
    <div class="field area">Please enter a brief description of your case</div>
    <div class="submit">SUBMIT</div>
  </form>
  <h2 class="abs contact-title">WHEN YOU CONTACT<b>DORIAN KESSLY LAW FOR</b><b>A FREE CONSULTATION</b></h2>
  <div class="abs contact-rule"></div>
  <div class="abs contact-copy">
    <p>Lorem ipsum dolor sit amet, consectetur adipiscing elit, sed do eiusmod tempor incididunt ut labore.</p>
    <p>Lorem ipsum dolor sit amet, consectetur adipiscing elit, sed do eiusmod tempor incididunt ut labore et dolore magna aliqua. Ut enim ad minim veniam, quis nostrud exercitation.</p>
  </div>
</section>

<footer>
  <div class="abs foot-brand">
    <div class="foot-mark"></div>
    <div class="foot-name">DORIAN KESSLY LAW<small>A PROFESSIONAL CORPORATION</small></div>
  </div>
  <div class="abs foot-col" style="left:522px;top:2565px">
    <h3>CONTACT US</h3>
    <div class="rule"></div>
    <p>4720 LARKFIELD AVE.<br>SUITE #210<br>ELK GROVE, CA 95758</p>
    <div class="social"><span></span><span></span><span></span></div>
  </div>
  <div class="abs foot-col" style="left:855px;top:2561px">
    <h3>QUICK LINKS</h3>
    <div class="rule"></div>
    <p>HOME<br>DORIAN KESSLY<br>PRACTICE AREAS<br>INSIGHTS<br>CONTACT<br>PRIVACY POLICY</p>
  </div>
  <div class="abs foot-divider"></div>
  <p class="abs disclaimer">The information on this website is for general information purposes only. Nothing on this site should be taken as legal advice for any individual case or situation. This information is not intended to create, and receipt of viewing does not constitute an attorney-client relationship.</p>
  <p class="abs copyright">© Copyright 2021 All Rights Reserved</p>
</footer>

</body>
</html>
```